TWB Shark card

This is a serious business card for a retired attorney with a sarcastic sense of humor. Incorporate into the design: shark with the tag line, Peaceful unless pressed. The image could be graphic but not comic. The card should have a classic, sophisticated, professional look. Partial to minimalist, even Asian designs. Color options are black/ white (though this can easily go too cartoonish), gray tones, blue gray tones, blue. Open to something unexpected, even color, as long as the look is professional. The shark image attached is what we've been using but it isn't a design requirement.(Not sure why entire image isn't visible.)

No company Harold T Quenby Name should be more prominent than the tag

This is the first time I've done this, so I apologize for not posting all this info up front. Some of it was in the narrative but to make it easier, I'm listing all the info that should be on the card. Harold T Quenby Attorney at STILL WATER image Peaceful unless pressed 58127 Willow Basin Street Harbor Vale, CA 90417 415-872-3091 hquenby@postvale.com There is no company. The tag, Peaceful unless pressed, should be less prominent than the name.

Industry/Entity Type

Attorney

Contact Information for Business Card

58127 Willow Basin Street
Harbor Vale, CA 90417
415-872-3091
hquenby@postvale.com

```html
<!DOCTYPE html>
<html lang="en">
<head>
<meta charset="utf-8">
<title>Harold T. Quenby – Business Card</title>
<link href="https://fonts.googleapis.com/css2?family=Noto+Serif:wght@400;500&display=swap" rel="stylesheet">
<style>
  :root {
    --backdrop: #0c0c0c;
    --card: #f6f6f6;
    --ink: #141414;
    --rule: #2a2a2a;
  }
  html, body {
    margin: 0;
    padding: 0;
    width: 1200px;
    height: 1000px;
    overflow: hidden;
    background: var(--backdrop);
  }
  .stage {
    position: relative;
    width: 1200px;
    height: 1000px;
    font-family: "Noto Serif", Georgia, serif;
    color: var(--ink);
  }
  .card {
    position: absolute;
    left: 258px;
    width: 680px;
    height: 387px;
    background: var(--card);
    box-shadow: 0 4px 18px rgba(0,0,0,0.6);
  }
  .card-front { top: 82px; }
  .card-back { top: 526px; }

  .brand { position: absolute; }
  .brand-dot {
    position: absolute;
    border-radius: 50%;
    background: var(--ink);
  }
  .brand-name {
    position: absolute;
    margin: 0;
    font-weight: 400;
    white-space: nowrap;
    letter-spacing: -0.2px;
    line-height: 1;
  }
  .brand-tagline {
    position: absolute;
    margin: 0;
    white-space: nowrap;
    line-height: 1;
  }

  /* Front */
  .card-front .brand-dot { left: 105px; top: 138px; width: 122px; height: 122px; }
  .card-front .brand-name { left: 239px; top: 166px; font-size: 50px; }
  .card-front .brand-tagline { left: 240px; top: 218px; font-size: 20px; letter-spacing: 2.6px; }

  /* Back */
  .card-back .brand-dot { left: 24px; top: 27px; width: 82px; height: 82px; }
  .card-back .brand-name { left: 114px; top: 43px; font-size: 34px; }
  .card-back .brand-tagline { left: 116px; top: 79px; font-size: 14.5px; letter-spacing: 1.8px; }

  .holder-name {
    position: absolute;
    right: 25px;
    top: 214px;
    margin: 0;
    font-size: 27px;
    font-weight: 500;
    letter-spacing: -0.2px;
    line-height: 1;
    white-space: nowrap;
  }
  .title-rule {
    position: absolute;
    left: 13px;
    right: 11px;
    top: 246px;
    height: 20px;
    display: flex;
    align-items: center;
  }
  .title-rule .line { height: 1px; background: var(--rule); }
  .title-rule .line-long { flex: 1; }
  .title-rule .line-short { width: 22px; }
  .title-rule .role {
    font-size: 17px;
    padding: 0 3px;
    line-height: 1;
    position: relative;
    top: 1px;
  }

  .contact-list {
    position: absolute;
    left: 28px;
    top: 270px;
    margin: 0;
    padding: 0;
    list-style: none;
    font-size: 19.5px;
    letter-spacing: 0.9px;
    line-height: 25px;
  }
  .contact-list li { display: flex; align-items: flex-start; }
  .contact-list .icon {
    width: 16px;
    height: 16px;
    margin-right: 7px;
    margin-top: 5px;
    flex: none;
  }
  .contact-list .address { line-height: 23px; margin-top: 1px; }
</style>
</head>
<body>
<div class="stage">

  <section class="card card-front">
    <div class="brand">
      <span class="brand-dot"></span>
      <h1 class="brand-name">STILL WATER</h1>
      <p class="brand-tagline">Peaceful unless pressed</p>
    </div>
  </section>

  <section class="card card-back">
    <div class="brand">
      <span class="brand-dot"></span>
      <p class="brand-name">STILL WATER</p>
      <p class="brand-tagline">Peaceful unless pressed</p>
    </div>

    <h2 class="holder-name">Harold T. Quenby</h2>
    <div class="title-rule">
      <span class="line line-long"></span>
      <span class="role">Attorney</span>
      <span class="line line-short"></span>
    </div>

    <ul class="contact-list">
      <li>
        <svg class="icon" viewBox="0 0 16 16" aria-hidden="true">
          <path d="M1 6c0-2 3-3 7-3s7 1 7 3v1.5h-3.5V6H4.5v1.5H1z" fill="#141414"/>
          <path d="M3.5 8.5h9l1.5 5H2z" fill="#141414"/>
          <circle cx="8" cy="11" r="1.6" fill="#f6f6f6"/>
        </svg>
        <span>415-872-3091</span>
      </li>
      <li>
        <svg class="icon" viewBox="0 0 16 16" aria-hidden="true">
          <rect x="1" y="3" width="14" height="10" fill="#141414"/>
          <path d="M1.5 3.5 8 9l6.5-5.5" fill="none" stroke="#f6f6f6" stroke-width="1.2"/>
        </svg>
        <span>hquenby@postvale.com</span>
      </li>
      <li>
        <svg class="icon" viewBox="0 0 16 16" aria-hidden="true">
          <path d="M8 1a4.5 4.5 0 0 0-4.5 4.5C3.5 9 8 15 8 15s4.5-6 4.5-9.5A4.5 4.5 0 0 0 8 1z" fill="#141414"/>
          <circle cx="8" cy="5.5" r="1.8" fill="#f6f6f6"/>
        </svg>
        <span class="address">58127 Willow Basin Street<br>Harbor Vale, CA 90417</span>
      </li>
    </ul>
  </section>

</div>
</body>
</html>
```